Redesign of an insurance website

Attached is an insurance website that I need to redesign. Currently the website is too dark. I like for example www.brenvalo.com . Could you make the website lighter and change the structure a little so that it is more user friendly?

Industry/Entity Type

Insurance

Number of Pages Required

4 page

```html
<!DOCTYPE html>
<html lang="cs">
<head>
<meta charset="utf-8">
<title>Kryjeme.cz – Srovnání pojištění</title>
<link href="https://fonts.googleapis.com/css2?family=Ubuntu:wght@400;500;700&family=Fira+Sans+Condensed:wght@500;600&display=swap" rel="stylesheet">
<style>
:root{
  --blue:#2f86f5;
  --orange:#fb7d1b;
  --ink:#222;
  --muted:#555;
  --line:#d6d6d6;
  --grey-band:#efefef;
  --footer:#2a2a2a;
  --footer-dark:#161616;
  --white:#fff;
}
*{margin:0;padding:0;box-sizing:border-box}
html,body{width:667px;height:1200px;overflow:hidden;background:var(--white)}
body{position:relative;font-family:"Ubuntu",Arial,sans-serif;color:var(--ink)}
.abs{position:absolute}
.heading{font-family:"Fira Sans Condensed","Arial Narrow",sans-serif;font-weight:600;text-transform:uppercase;color:var(--orange);text-align:center;left:0;width:667px}

/* header */
.site-header{left:0;top:0;width:667px;height:48px;background:var(--white);border-top:2px solid var(--blue)}
.brand{left:62px;top:13px;font:700 21px "Ubuntu",sans-serif;color:var(--blue);letter-spacing:.5px}
.social{top:5px;width:13px;height:13px;border-radius:50%}
.tab{top:0;height:18px;color:var(--white);font-size:8px;font-weight:500;line-height:18px;text-align:center}
.tab-register{left:448px;width:82px;background:var(--blue);border-radius:0 0 0 8px}
.tab-login{left:528px;width:88px;background:var(--orange);border-radius:0 0 10px 0}
.main-nav a{position:absolute;top:32px;font-size:8px;font-weight:700;color:var(--ink);text-decoration:none}
.main-nav a.active{color:var(--orange)}

/* hero */
.hero-photo{left:0;top:48px;width:667px;height:275px;background:linear-gradient(120deg,#3a434d 0%,#59626b 45%,#3b424a 75%,#2c3238 100%)}
.hero-title{left:63px;top:93px;font-size:14.5px;color:var(--orange)}
.hero-title span{color:#4d9bff}
.cover{width:70px;text-align:center;color:var(--white);font-size:6.5px}
.cover .ring{width:34px;height:34px;border:1px solid var(--white);border-radius:50%;margin:0 auto 4px}
.slider-dots{left:196px;top:260px}
.slider-dots i{display:inline-block;width:4px;height:4px;border-radius:50%;background:var(--white);margin-right:2px}
.slider-dots i.on{background:var(--orange)}

.quote-form{left:432px;top:96px;width:172px;height:187px;background:rgba(225,225,225,.93)}
.quote-form .head{height:48px;background:var(--orange);color:var(--white);font-weight:700;font-size:9.6px;text-align:center;padding-top:21px}
.quote-form .badge{left:72px;top:-13px;width:28px;height:28px;border-radius:50%;background:var(--white)}
.field{position:absolute;left:13px;width:145px;height:18px;background:var(--white);font-size:6.5px;font-style:italic;color:#888;padding:5px 8px}
.agree{left:13px;top:140px;font-size:6px;color:#333}
.agree i{display:inline-block;width:6px;height:6px;background:var(--white);border:1px solid #bbb;margin-right:6px;vertical-align:-1px}
.form-btn{left:13px;top:156px;width:145px;height:20px;background:var(--blue);color:var(--white);font-size:8px;font-weight:700;text-align:center;line-height:20px}

/* benefits */
.divider{left:192px;width:284px;height:1px;background:var(--line)}
.divider::after{content:"";position:absolute;left:137px;top:-4px;width:9px;height:5px;border:1px solid #999;border-bottom:none;border-radius:9px 9px 0 0;background:var(--white)}
.grey .divider::after{background:var(--grey-band)}
.benefit h3{font-size:7.5px;font-weight:700;color:var(--blue);text-transform:uppercase;letter-spacing:.3px;margin-bottom:4px}
.benefit p{font-size:6.8px;line-height:1.5;color:var(--ink)}
.right{text-align:right}
.person-photo{left:282px;top:512px;width:104px;height:131px;background:linear-gradient(180deg,#d9dadc 0%,#6e7276 55%,#3f4347 100%)}

/* reasons band */
.grey{left:0;top:643px;width:667px;height:199px;background:var(--grey-band)}
.lead{left:70px;top:85px;width:528px;font-size:7px;line-height:1.75;text-align:center;color:var(--ink)}
.pill{height:21px;border-radius:11px;background:var(--blue);color:var(--white);font-size:8.5px;font-weight:700;text-align:center;line-height:21px}

/* steps */
.step{width:130px;text-align:center}
.step h4{font-size:8px;font-weight:700;color:var(--orange);margin-bottom:4px}
.step p{font-size:6px;line-height:1.35;color:var(--ink)}

/* footer */
.footer-top{left:0;top:1140px;width:667px;height:34px;background:var(--footer)}
.newsletter{left:63px;top:10px;width:119px;height:16px;background:var(--white);font-size:6px;padding:5px 5px;color:#222}
.confirm{left:182px;top:10px;width:63px;height:16px;background:var(--orange);color:var(--white);font-size:7px;font-weight:700;letter-spacing:1px;text-align:center;line-height:16px}
.footer-nav a{position:absolute;top:13px;font-size:6px;font-weight:700;color:var(--white);text-decoration:none}
.footer-bottom{left:0;top:1174px;width:667px;height:26px;background:var(--footer-dark);color:var(--white)}
.copyright{left:63px;top:10px;font-size:6.4px;font-weight:500}
.footer-brand{left:341px;top:7px;font:700 11px "Ubuntu",sans-serif;color:var(--blue);letter-spacing:.4px}
.follow{left:514px;top:9px;font-size:7px}
.follow-dot{top:5px;width:15px;height:15px;border:1px solid var(--white);border-radius:50%}
</style>
</head>
<body>

<header class="abs site-header">
  <div class="abs brand">KRYJEME.CZ</div>
  <span class="abs social" style="left:388px;background:#3b5b98"></span>
  <span class="abs social" style="left:406px;background:#2a9ee8"></span>
  <span class="abs social" style="left:425px;background:#d9432f"></span>
  <div class="abs tab tab-register">Registrovat</div>
  <div class="abs tab tab-login">Přihlásit Se</div>
  <nav class="main-nav">
    <a class="active" style="left:418px">O NÁS</a>
    <a style="left:473px">C'ASTE 'DOTAZY</a>
    <a style="left:567px">KONTAKT</a>
  </nav>
</header>

<section>
  <div class="abs hero-photo" role="img" aria-label="Tmavá fotografie pojistné smlouvy, kalkulačky a stetoskopu"></div>
  <h1 class="abs hero-title" style="font-weight:400">Chceš Pojistit <span>Něco Jiného?</span></h1>

  <div class="abs cover" style="left:57px;top:127px"><div class="ring"></div>Cestovní Pojištění</div>
  <div class="abs cover" style="left:131px;top:127px"><div class="ring"></div>Havarijní Pojištění</div>
  <div class="abs cover" style="left:207px;top:127px"><div class="ring"></div>Domova Pojištění</div>
  <div class="abs cover" style="left:283px;top:127px"><div class="ring"></div>Pojištění Auta</div>
  <div class="abs cover" style="left:57px;top:193px"><div class="ring"></div>Pojištění Lodí</div>
  <div class="abs cover" style="left:126px;top:193px;width:80px"><div class="ring"></div>Pojištění Motocyklu</div>
  <div class="abs cover" style="left:202px;top:193px;width:80px"><div class="ring"></div>Pojištění Nájemníků</div>
  <div class="abs cover" style="left:283px;top:193px"><div class="ring"></div>Pojištění Zvířat</div>

  <svg class="abs" style="left:360px;top:182px" width="12" height="16" viewBox="0 0 12 16"><path d="M3 2l6 6-6 6" fill="none" stroke="#3d8ef7" stroke-width="2"/></svg>
  <div class="abs slider-dots"><i class="on"></i><i></i><i></i></div>

  <form class="abs quote-form">
    <div class="head">Najdeme Nejvhodnější Pojištění</div>
    <div class="abs badge"></div>
    <div class="field" style="top:41px">název</div>
    <div class="field" style="top:64px">příjmení</div>
    <div class="field" style="top:87px">E-mail</div>
    <div class="field" style="top:110px">Telefon</div>
    <div class="abs agree"><i></i>Souhlasím S Podmínkami Používání</div>
    <div class="abs form-btn">SPOCI'TAT CENU</div>
  </form>
</section>

<section>
  <h2 class="abs heading" style="top:361px;font-size:15.5px">Proc hledat pojisteni pres Kryjeme.cz?</h2>
  <div class="abs divider" style="top:392px"></div>

  <svg class="abs" style="left:0;top:460px" width="667" height="183" viewBox="0 460 667 183">
    <path d="M206 643 A128 128 0 0 1 462 643" fill="none" stroke="#4e95f5" stroke-width="9"/>
    <g fill="#fff" stroke="#2f86f5" stroke-width="1.2">
      <circle cx="334" cy="510" r="3"/><circle cx="397" cy="527" r="3"/><circle cx="439" cy="569" r="3"/><circle cx="458" cy="612" r="3"/>
      <circle cx="271" cy="527" r="3"/><circle cx="229" cy="569" r="3"/><circle cx="209" cy="612" r="3"/>
    </g>
    <g fill="#fff" stroke="#2f86f5" stroke-width="1.3">
      <circle cx="334" cy="479" r="22"/><circle cx="410" cy="499" r="22"/><circle cx="466" cy="546" r="22"/><circle cx="494" cy="610" r="22"/>
      <circle cx="256" cy="499" r="22"/><circle cx="201" cy="546" r="22"/><circle cx="173" cy="610" r="22"/>
    </g>
    <g fill="#fb7d1b">
      <path d="M322 480l7-6 5 3 5-3 7 6-8 7-4-3-4 3z"/>
      <circle cx="408" cy="497" r="9" fill="none" stroke="#fb7d1b" stroke-width="3"/><rect x="414" y="499" width="7" height="8"/>
      <ellipse cx="469" cy="549" rx="10" ry="7"/><circle cx="460" cy="540" r="6"/>
      <rect x="484" y="602" width="8" height="8"/><rect x="497" y="602" width="8" height="8"/><rect x="490" y="613" width="8" height="9"/>
      <path d="M245 498a11 9 0 0 1 22 0z"/><circle cx="256" cy="505" r="5"/>
      <path d="M190 548l11-10 11 10v10h-22z"/>
      <circle cx="173" cy="610" r="10" fill="none" stroke="#fb7d1b" stroke-width="2"/><path d="M163 610h20M173 600v20" stroke="#fb7d1b" stroke-width="1.5"/>
    </g>
  </svg>
  <div class="abs person-photo" role="img" aria-label="Fotografie usměvavého pojišťovacího poradce v obleku"></div>

  <div class="abs benefit" style="left:254px;top:411px;width:160px;text-align:center"><h3>Nejlepší obchod</h3><p>snámi najdete tu nejvýhodnější<br>nabídku</p></div>
  <div class="abs benefit right" style="left:112px;top:474px;width:110px"><h3>Všechny druhy</h3><p>zařídime vám všechny<br>druhy pojištění</p></div>
  <div class="abs benefit right" style="left:58px;top:524px;width:110px"><h3>Z domova</h3><p>vše vyřídite z pohodlí<br>domova</p></div>
  <div class="abs benefit right" style="left:32px;top:591px;width:110px"><h3>Nechoďte nikam</h3><p>nemusite nikam chodit<br>a ušetříte</p></div>
  <div class="abs benefit" style="left:445px;top:474px;width:110px"><h3>Nejlepší cena</h3><p>zaručíme vám nejlepší<br>cenu na trhu</p></div>
  <div class="abs benefit" style="left:502px;top:526px;width:110px"><h3>Šetřit peníze</h3><p>stačí pár minut a můžete<br>ušetřit tisíce</p></div>
  <div class="abs benefit" style="left:530px;top:593px;width:110px"><h3>Srovnání</h3><p>srovnáváme všechny<br>pojišťovny</p></div>
</section>

<section class="abs grey">
  <h2 class="abs heading" style="top:36px;font-size:12.5px">Uzavřeli jste v minulosti nevýhodnou pojistku?&nbsp; Zbavte se jí!</h2>
  <div class="abs divider" style="top:63px"></div>
  <p class="abs lead">Lorem ipsum dolor sit amet, consectetuer adipiscing elit, sed diam nonummy nibh euismod tincidunt ut laoreet dolore magna aliquam erat volutpat. Ut wisi enim ad minim veniam, quis nostrud exerci tation ullamcorper suscipit lobortis nisl ut aliquip ex ea commodo consequat. Duis autem vel eum iriur nisl ut aliquip ex ea&nbsp; am erat volutpat. Ut wisi enim ad minim veniam, quis nostrud exerci tation ullamcorperad minim veniam, quismagna aliquam erat volutpat.</p>
  <div class="abs pill" style="left:293px;top:137px;width:81px">SPOCITAT CENU</div>
</section>

<section>
  <h2 class="abs heading" style="top:878px;font-size:15px">Jak to funguje</h2>
  <div class="abs divider" style="top:909px"></div>

  <svg class="abs" style="left:0;top:920px" width="667" height="100" viewBox="0 920 667 100">
    <defs><radialGradient id="disc" cx=".5" cy=".4" r=".6"><stop offset="0" stop-color="#fff"/><stop offset="1" stop-color="#e4e4e4"/></radialGradient></defs>
    <g stroke-width="5" fill="url(#disc)">
      <circle cx="111" cy="968" r="36" stroke="#fb7d1b"/><circle cx="258" cy="968" r="36" stroke="#2f86f5"/>
      <circle cx="405" cy="968" r="36" stroke="#fb7d1b"/><circle cx="552" cy="968" r="36" stroke="#2f86f5"/>
    </g>
    <path d="M105 1006h12l-6 7z" fill="#fb7d1b"/><path d="M252 1006h12l-6 7z" fill="#2f86f5"/>
    <path d="M399 1006h12l-6 7z" fill="#fb7d1b"/><path d="M546 1006h12l-6 7z" fill="#2f86f5"/>
    <g fill="none" stroke-width="1.2">
      <path d="M168 970q14-8 32 0m-4-4l4 4-5 2" stroke="#fb7d1b"/>
      <path d="M316 970q14-8 32 0m-4-4l4 4-5 2" stroke="#2f86f5"/>
      <path d="M463 970q14-8 32 0m-4-4l4 4-5 2" stroke="#fb7d1b"/>
    </g>
    <g fill="none" stroke="#fb7d1b" stroke-width="2"><rect x="101" y="955" width="18" height="24"/><path d="M105 962h10M105 967h10M105 972h6"/></g>
    <path d="M258 953l12 4v8c0 8-6 13-12 15-6-2-12-7-12-15v-8z" fill="none" stroke="#2f86f5" stroke-width="2"/>
    <path d="M252 966l5 5 8-9" fill="none" stroke="#2f86f5" stroke-width="2"/>
    <path d="M389 969l9-8 7 4 7-4 9 8-10 9-6-4-6 4z" fill="#fb7d1b"/>
    <path d="M542 966h6v15h-6zM550 966l6-12c4 0 4 4 3 8h8c2 0 3 2 2 4l-3 12c0 2-2 3-4 3h-12z" fill="#2f86f5"/>
  </svg>

  <div class="abs step" style="left:46px;top:1020px"><h4>Fill Up the form</h4><p>Lorem ipsum dolor sit amet,conse<br>ctetuer aliquam erat volutpat</p></div>
  <div class="abs step" style="left:193px;top:1020px"><h4>Verfication</h4><p>Lorem ipsum dolor sit amet,conse<br>ctetuer aliquam erat volutpat</p></div>
  <div class="abs step" style="left:340px;top:1020px"><h4>Closing</h4><p>Lorem ipsum dolor sit amet,conse<br>ctetuer aliquam erat volutpat</p></div>
  <div class="abs step" style="left:487px;top:1020px"><h4>You Are Done</h4><p>Lorem ipsum dolor sit amet,conse<br>ctetuer aliquam erat volutpat</p></div>

  <div class="abs pill" style="left:293px;top:1082px;width:81px">CHCI UŠETŘIT</div>
</section>

<footer>
  <div class="abs footer-top">
    <div class="abs newsletter">Email</div>
    <div class="abs confirm">POTVRDIT</div>
    <nav class="footer-nav">
      <a style="left:311px">O NÁS</a>
      <a style="left:345px">C'ASTE 'DOTAZY</a>
      <a style="left:410px">KONTAKT</a>
      <a style="left:453px">OCHRANA SOUKROMI</a>
      <a style="left:544px">PODMINKY POUZITI</a>
    </nav>
  </div>
  <div class="abs footer-bottom">
    <div class="abs copyright">Copyright © 2017 Kryjeme.cz.&nbsp; Všechna Práva Vyhrazena.</div>
    <div class="abs footer-brand">KRYJEME.CZ</div>
    <div class="abs follow">Follow Us</div>
    <span class="abs follow-dot" style="left:552px"></span>
    <span class="abs follow-dot" style="left:571px"></span>
    <span class="abs follow-dot" style="left:590px"></span>
  </div>
</footer>

</body>
</html>
```